Federal Government Proposal Development Consulting company needs a website designed and coded

I am looking for someone to design (using an existing logo, color palette, and text fonts) and code a wordpress-based website for a Proposal Development consulting company. I have full copy for all site pages and suggestions for images/ graphics and a few example design templates to go from.

One note, from a color perspective - I included a mockup of a business card to highlight a color scheme that I tend to like - if you look at the back of the business card, the blend of the grey, blue, with the neon green highlight as a separator really seems to pop. Just a thought as you are designing the page.

I would like to see 2-3 potential design layouts, and I will select one to move forward with. Then, I would like the site to be coded for WordPress (I can provide a login to my wordpress site). I would like 1 opportunity to review the coded site and make any final tweaks.

```html
<!DOCTYPE html>
<html lang="en">
<head>
<meta charset="utf-8">
<title>Penwell Consulting — Proposal Development</title>
<link rel="stylesheet" href="https://fonts.googleapis.com/css2?family=Marcellus&family=Lato:wght@400;700&display=swap">
<style>
:root{
  --navy:#161a63;
  --navy-deep:#0f1250;
  --blue:#2a36b4;
  --blue-bright:#3446d6;
  --cyan:#5fe4f2;
  --cyan-soft:#b9f4fa;
  --ink:#1d1d2b;
  --muted:#6b6e80;
  --line:#e3e5ee;
  --paper:#ffffff;
  --soft:#f5f6fa;
}
*{box-sizing:border-box;margin:0;padding:0}
html,body{width:1200px;height:4168px;overflow:hidden}
body{font-family:"Lato",Arial,sans-serif;color:var(--ink);background:var(--paper);font-size:15px;line-height:1.6}
h1,h2,h3,.serif{font-family:"Marcellus",Georgia,serif;font-weight:400}
.btn{display:inline-block;background:var(--blue);color:#fff;font-size:13px;font-weight:700;padding:11px 26px;border-radius:3px;text-decoration:none}
.img-fill{display:block}

/* header */
.topbar{height:34px;background:var(--navy);color:#fff;font-size:12px;display:flex;justify-content:flex-end;align-items:center;gap:26px;padding:0 60px}
.site-header{height:86px;display:flex;align-items:center;justify-content:space-between;padding:0 60px;border-bottom:1px solid var(--line)}
.brand{display:flex;align-items:center;gap:10px;font-family:"Marcellus",Georgia,serif;font-size:24px;color:var(--navy)}
.brand-dot{width:14px;height:14px;border-radius:50%;background:var(--blue)}
.nav{display:flex;gap:32px;font-size:14px;font-weight:700;color:var(--navy)}
.nav .active{color:var(--blue);border-bottom:2px solid var(--blue);padding-bottom:4px}

/* hero */
.hero{position:relative;height:470px;overflow:hidden}
.hero-media{position:absolute;inset:0;background:linear-gradient(100deg,#1a2280 0%,#3a4fc0 45%,#8fa6d8 75%,#c8b48a 100%)}
.hero-copy{position:relative;padding:120px 0 0 90px;color:#fff;max-width:620px}
.hero-copy h1{font-size:52px;line-height:1.1}
.hero-copy p{font-size:22px;margin:14px 0 28px}
.hero-wave{position:absolute;bottom:0;left:0}

/* what we do */
.what{padding:60px 120px 80px;text-align:center}
.section-title{font-size:40px;color:var(--navy);margin-bottom:24px}
.what .lead{font-size:14px;color:var(--muted);max-width:900px;margin:0 auto 18px}
.cards{display:flex;gap:34px;margin-top:44px;text-align:left}
.card{flex:1;border:1px solid var(--line);box-shadow:0 6px 22px rgba(22,26,99,.08);padding:30px 28px;border-radius:4px}
.card h3{font-size:21px;color:var(--navy);margin-bottom:12px}
.card p{font-size:14px;color:var(--muted)}
.card .more{display:inline-block;margin-top:18px;font-size:13px;font-weight:700;color:var(--blue)}

/* who we are */
.who{position:relative;height:470px}
.who-text{position:absolute;left:170px;right:170px;top:110px;text-align:center}
.who-text p{font-size:14px;color:var(--ink);margin:18px 0 24px}
.who-quill{position:absolute;left:50px;top:330px;width:140px;height:110px;border-radius:6px}

/* services */
.services{display:flex;padding:70px 60px 60px;gap:40px}
.services-list{flex:1}
.services-list h2{font-size:36px;color:var(--navy);margin-bottom:22px}
.svc-cols{display:flex;gap:40px}
.svc-cols ul{list-style:none;flex:1}
.svc-cols li{font-size:15px;padding:9px 0;border-bottom:1px solid var(--line);display:flex;align-items:center;gap:10px}
.svc-cols li::before{content:"";width:8px;height:8px;background:var(--blue);border-radius:50%}
.svc-cols li.hl{color:var(--blue);font-weight:700}
.services .btn{margin-top:28px}
.services-media{width:360px;height:440px;border-radius:6px;background:linear-gradient(160deg,#dfe5f3,#9aaad4 60%,#e5c685)}

/* expertise */
.expertise{background:var(--soft);padding:60px 60px 70px;text-align:center}
.exp-row{display:flex;align-items:center;gap:24px;margin:30px 0 36px}
.arrow{width:40px;height:40px;border-radius:50%;background:#fff;border:1px solid var(--line);display:flex;align-items:center;justify-content:center;flex-shrink:0}
.exp-tile{flex:1;height:210px;border-radius:4px;background:linear-gradient(160deg,#2c3ab0,#161a63);color:#fff;display:flex;align-items:flex-end;padding:18px;font-family:"Marcellus",Georgia,serif;font-size:18px}

/* contact */
.contact{position:relative;height:570px;color:#fff}
.contact-inner{position:absolute;left:170px;right:170px;top:120px;text-align:center}
.contact-inner h2{font-size:40px;margin-bottom:28px}
.form-grid{display:grid;grid-template-columns:1fr 1fr;gap:16px}
.field{height:44px;background:#fff;border-radius:3px;color:var(--muted);font-size:14px;text-align:left;padding:12px 16px}
.field.wide{grid-column:1/3;height:110px}
.contact .btn{margin-top:24px;background:var(--blue-bright)}

/* testimonials */
.clients{padding:70px 60px 60px;text-align:center}
.quotes{display:flex;gap:30px;margin:30px 0 36px;text-align:left}
.quote{flex:1;border:1px solid var(--line);border-radius:4px;padding:28px;box-shadow:0 6px 22px rgba(22,26,99,.07)}
.stars{color:#f2b01e;font-size:16px;letter-spacing:3px}
.quote p{font-size:14px;color:var(--muted);margin:12px 0 20px}
.who-line{display:flex;align-items:center;gap:12px;font-weight:700;font-size:14px;color:var(--navy)}
.avatar{width:42px;height:42px;border-radius:50%;background:linear-gradient(135deg,#c9cfe3,#8b96c2)}

/* footer */
.site-footer{position:relative;height:556px;color:#fff}
.footer-cols{position:absolute;top:150px;left:90px;right:90px;display:flex;gap:60px}
.footer-cols h4{font-size:16px;margin-bottom:16px}
.footer-cols p,.footer-cols li{font-size:13px;color:#cfd3f2;list-style:none;margin-bottom:8px}
.footer-brand{width:320px;font-family:"Marcellus",Georgia,serif;font-size:34px}
.socials{display:flex;gap:10px}
.socials span{width:32px;height:32px;border-radius:50%;background:rgba(255,255,255,.2)}
.footer-bottom{position:absolute;bottom:40px;left:90px;right:90px;border-top:1px solid rgba(255,255,255,.2);padding-top:18px;font-size:12px;color:#cfd3f2;display:flex;gap:80px}
</style>
</head>
<body>

<div class="topbar"><span>(555) 014-2290</span><span>hello@penwellconsulting.com</span></div>
<header class="site-header">
  <div class="brand"><span class="brand-dot"></span>Penwell Consulting</div>
  <nav class="nav">
    <span class="active">Home</span><span>Who We Are</span><span>About Us</span><span>Contact Us</span>
  </nav>
  <a class="btn">Book a Free Consultation</a>
</header>

<section class="hero">
  <div class="hero-media" role="img" aria-label="Photo of two engineers in hard hats reviewing plans on a construction site"></div>
  <div class="hero-copy">
    <h1>Generate Success</h1>
    <p>Fuel Innovation in Proposal Excellence with <strong>Penwell Consulting</strong></p>
    <a class="btn">Click Here to Review Our Services</a>
  </div>
  <svg class="hero-wave" width="1200" height="70" viewBox="0 0 1200 70">
    <path d="M0 30 L600 62 L1200 30 L1200 70 L0 70Z" fill="#fff"/>
    <path d="M0 30 L600 62 L1200 30" fill="none" stroke="#2a36b4" stroke-width="4"/>
  </svg>
</section>

<section class="what">
  <h2 class="section-title">What We Do</h2>
  <p class="lead">We partner with federal contractors to plan, write and deliver winning proposals. Our team brings decades of capture, compliance and writing experience to every bid, so your response is clear, compliant and compelling from the first page to the last.</p>
  <p class="lead">Welcome to Penwell Consulting, your partner in proposal excellence. We combine <strong>proven methods</strong> and modern tools to give your team a <strong>real advantage</strong> and deliver measurable results.</p>
  <div class="cards">
    <article class="card">
      <h3>Capture Management</h3>
      <p>We help you shape opportunities early, know the customer, map the competition and build a win strategy long before the solicitation is released.</p>
      <span class="more">Read More →</span>
    </article>
    <article class="card">
      <h3>Proposal Development</h3>
      <p>From outline to final production, we manage schedules, write persuasive sections and keep every volume fully compliant with the request.</p>
      <span class="more">Read More →</span>
    </article>
    <article class="card">
      <h3>Generative AI</h3>
      <p>We apply secure AI tools to speed drafting, reuse past content and free your experts to focus on the strategy that wins awards.</p>
      <span class="more">Read More →</span>
    </article>
  </div>
</section>

<section class="who">
  <svg width="1200" height="470" viewBox="0 0 1200 470" style="position:absolute;inset:0">
    <polygon points="0,60 300,0 900,0 1200,60 1200,410 900,470 300,470 0,410" fill="#2a36b4"/>
    <polygon points="0,75 310,18 890,18 1200,75 1200,395 890,452 310,452 0,395" fill="#5fe4f2"/>
    <polygon points="140,90 360,40 840,40 1060,90 1060,380 840,430 360,430 140,380" fill="#b9f4fa" opacity=".7"/>
  </svg>
  <div class="who-text">
    <h2 class="section-title">Who We Are</h2>
    <p>We are a small team of seasoned proposal managers, writers and capture experts who have supported contractors of every size. Our people have sat on both sides of the table, so we know what evaluators look for and how to present your solution with clarity. We work as an extension of your team, bringing structure, calm and accountability to even the tightest deadlines.</p>
    <a class="btn">About Us</a>
  </div>
  <div class="who-quill img-fill" role="img" aria-label="Illustration of a quill pen" style="background:linear-gradient(135deg,#2a36b4,#161a63)"></div>
</section>

<section class="services">
  <div class="services-list">
    <h2>Our Services</h2>
    <div class="svc-cols">
      <ul>
        <li>Generative AI</li>
        <li>How to Win / Competitive Intelligence</li>
        <li class="hl">Proposal Workshop</li>
        <li>Executive Summaries</li>
        <li>Storyboard Writer</li>
        <li>Resume Writer</li>
        <li>Color Team Reviews</li>
        <li>Black Hat Facilitation</li>
        <li>Proposal Production</li>
      </ul>
      <ul>
        <li>Technical Sr. Writer</li>
        <li>Capture Management</li>
        <li>Compliance Review</li>
        <li>Pricing Support</li>
        <li>Book Boss</li>
        <li>Past Performance Writer</li>
        <li>Orals Coaching</li>
        <li>Graphics Design</li>
        <li>Subcontract Management</li>
      </ul>
    </div>
    <a class="btn">Explore More</a>
  </div>
  <div class="services-media img-fill" role="img" aria-label="Photo of an engineer in a hard hat with blueprints"></div>
</section>

<section class="expertise">
  <h2 class="section-title">Subject Matter Expertise</h2>
  <div class="exp-row">
    <span class="arrow"><svg width="12" height="12" viewBox="0 0 12 12"><path d="M8 1 L3 6 L8 11" fill="none" stroke="#161a63" stroke-width="2"/></svg></span>
    <div class="exp-tile" role="img" aria-label="Photo for defense and aerospace">Defense</div>
    <div class="exp-tile" role="img" aria-label="Photo for health services">Health</div>
    <div class="exp-tile" role="img" aria-label="Photo for information technology">IT Services</div>
    <div class="exp-tile" role="img" aria-label="Photo for engineering and construction">Engineering</div>
    <span class="arrow"><svg width="12" height="12" viewBox="0 0 12 12"><path d="M4 1 L9 6 L4 11" fill="none" stroke="#161a63" stroke-width="2"/></svg></span>
  </div>
  <a class="btn">View All Expertise</a>
</section>

<section class="contact">
  <svg width="1200" height="570" viewBox="0 0 1200 570" style="position:absolute;inset:0">
    <polygon points="0,70 300,0 900,0 1200,70 1200,500 900,570 300,570 0,500" fill="#161a63"/>
    <polygon points="150,100 380,50 820,50 1050,100 1050,470 820,520 380,520 150,470" fill="#1f2577"/>
  </svg>
  <div class="contact-inner">
    <h2>Contact Us</h2>
    <div class="form-grid">
      <div class="field">Name</div>
      <div class="field">Email</div>
      <div class="field">Phone</div>
      <div class="field">Subject</div>
      <div class="field wide">Your message</div>
    </div>
    <a class="btn">Submit</a>
  </div>
</section>

<section class="clients">
  <h2 class="section-title">Happy Clients Say</h2>
  <div class="quotes">
    <article class="quote">
      <div class="stars">★★★★★</div>
      <p>Their team brought order to a chaotic bid and helped us submit a clean, compliant volume ahead of schedule. We won the award.</p>
      <div class="who-line"><span class="avatar"></span>Marcus Hale</div>
    </article>
    <article class="quote">
      <div class="stars">★★★★★</div>
      <p>Sharp writers, calm managers and real strategy. Our executive summary has never been stronger, and evaluators noticed it.</p>
      <div class="who-line"><span class="avatar"></span>Dana Ortiz</div>
    </article>
    <article class="quote">
      <div class="stars">★★★★★</div>
      <p>The review sessions were honest and useful. We fixed weak sections early and went into final production with confidence.</p>
      <div class="who-line"><span class="avatar"></span>Leo Ramsey</div>
    </article>
  </div>
  <a class="btn">View All</a>
</section>

<footer class="site-footer">
  <svg width="1200" height="556" viewBox="0 0 1200 556" style="position:absolute;inset:0">
    <polygon points="0,70 300,0 900,0 1200,70 1200,556 0,556" fill="#161a63"/>
    <polygon points="0,70 300,0 900,0 1200,70" fill="none" stroke="#2a36b4" stroke-width="4"/>
  </svg>
  <div class="footer-cols">
    <div class="footer-brand">Penwell Consulting</div>
    <div>
      <h4>Contact Us</h4>
      <p>(555) 014-2290</p>
      <p>hello@penwellconsulting.com</p>
      <p>120 Harbor Lane, Suite 4<br>Riverton, VA 00000</p>
    </div>
    <div>
      <h4>Quick Links</h4>
      <ul><li>Home</li><li>Who We Are</li><li>About Us</li><li>Contact Us</li></ul>
    </div>
    <div>
      <h4>Follow Us</h4>
      <div class="socials"><span></span><span></span><span></span></div>
    </div>
  </div>
  <div class="footer-bottom"><span>© 2024 Penwell Consulting LLC. All Rights Reserved.</span><span>Terms &amp; Conditions</span><span>Privacy Policy</span></div>
</footer>

</body>
</html>
```